Re-style home page - eye-catching and unique design for social commerce website

We need a new concept design for TrindaMo's home page.
We don't want to make huge changes but creating a more professional and eye-catching style.

We need to look very serious like a professional services company and in the same time to look like a social network for e-commerce.

Our logo is very captive and you can use to creating something of harmonious.

This is a re-style and I'm excepted to see unique and fresh design like Clovaret.

Target Market(s)

e-commerce and social

Industry/Entity Type

Social

Number of Pages Required

1 page

Font styles to use
Serif
Sans Serif

Requirements
Must have
• An eye-catching result.
• Search bar with logo and Login How it works and business
• The slogan with login and signup.
• Footer links.
Nice to have
• I would like to open the home page and see only two clear ways:
• -Consumer
• --Search
• --The slogan
• --Login and Signup
• --How it works
• -Business
• --Go to Business area
• Background: City, Shopping.
Should not have
• Scrollbar style!

```html
<!DOCTYPE html>
<html lang="en">
<head>
<meta charset="utf-8">
<title>TrindaMo – Shop directly from your profile</title>
<link rel="stylesheet" href="https://fonts.googleapis.com/css2?family=Open+Sans:wght@400;600;700&family=Russo+One&family=Roboto+Condensed:wght@700&display=swap">
<style>
:root{
  --chrome:#333333;
  --chrome-dark:#2b2b2b;
  --white:#ffffff;
  --muted:#d8d8d8;
  --orange:#e8633e;
  --brown:#4a2a1e;
  --accent-yellow:#f6e14c;
  --signup:#585d9c;
  --login:#e2325b;
  --photo-a:#8a8178;
  --photo-b:#b9aea6;
  --photo-c:#6f6a68;
}
*{box-sizing:border-box;margin:0;padding:0}
html,body{width:1200px;height:900px;overflow:hidden;background:var(--chrome)}
body{position:relative;font-family:"Open Sans",Arial,sans-serif;color:var(--white)}
.hero-photo{position:absolute;inset:0;width:1200px;height:900px}
.frame{position:absolute;inset:0}
.site-header{position:absolute;top:0;left:0;width:1200px;height:100px}
.brand{position:absolute;left:30px;top:16px;display:flex;align-items:center;gap:10px;font-weight:700;font-size:36px;letter-spacing:-0.5px;line-height:44px}
.brand-mark{width:22px;height:22px;background:var(--orange)}
.btn{position:absolute;top:35px;height:26px;border-radius:5px;border:0;color:var(--white);font:600 12px "Open Sans",Arial,sans-serif;display:flex;align-items:center;justify-content:center}
.btn-signup{left:573px;width:94px;background:var(--signup)}
.btn-login{left:1098px;width:77px;background:var(--login)}
.or{position:absolute;left:683px;top:40px;font-size:12px}
.field-label{position:absolute;top:15px;font-size:12px;font-weight:700}
.field{position:absolute;top:35px;width:188px;height:26px;background:var(--white);border-radius:5px;border:0}
.keep{position:absolute;left:713px;top:68px;display:flex;align-items:center;gap:6px;font-size:10px}
.keep span.box{width:11px;height:11px;background:var(--white);border-radius:2px}
.forgot{position:absolute;left:906px;top:68px;font-size:10px}
.feature{position:absolute;left:340px;top:215px;width:520px;height:520px}
.feature-copy{position:absolute;left:360px;top:255px;width:480px;text-align:center}
.basket{display:block;margin:0 auto;width:68px;height:68px}
.headline{font-family:"Russo One",Arial,sans-serif;font-size:40px;line-height:44px;margin-top:10px;color:var(--white)}
.subline{font-family:"Russo One",Arial,sans-serif;font-size:30px;line-height:32px;color:var(--brown)}
.divider{height:1px;background:rgba(255,255,255,.7);margin:20px auto 0;width:400px}
.categories{margin-top:22px;font-family:"Roboto Condensed",Arial,sans-serif;font-weight:700;font-size:14.5px;line-height:20px;text-transform:uppercase}
.categories span{margin:0 4px}
.categories .hl{color:var(--accent-yellow)}
.divider-low{width:360px;margin-top:28px}
.search-label{margin-top:30px;font-size:14px}
.search-field{display:block;margin:5px auto 0;width:187px;height:26px;background:var(--white);border:1px solid #ccc;border-radius:5px}
.footer-nav{position:absolute;left:27px;top:868px;display:flex;align-items:center;font-size:11px;color:var(--muted)}
.footer-nav .dot{width:4px;height:4px;border-radius:50%;background:var(--muted);margin:0 9px}
</style>
</head>
<body>
<svg class="hero-photo" viewBox="0 0 1200 900" role="img" aria-label="Photo of friends laughing while carrying shopping bags on a city street">
  <defs>
    <linearGradient id="photoTone" x1="0" y1="0" x2="1" y2="1">
      <stop offset="0" stop-color="var(--photo-b)"/>
      <stop offset=".5" stop-color="var(--photo-a)"/>
      <stop offset="1" stop-color="var(--photo-c)"/>
    </linearGradient>
  </defs>
  <rect width="1200" height="900" fill="url(#photoTone)"/>
</svg>

<svg class="frame" viewBox="0 0 1200 900" aria-hidden="true">
  <polygon points="0,0 1200,0 1200,100 0,76" fill="var(--chrome)"/>
  <polygon points="0,848 1200,868 1200,900 0,900" fill="var(--chrome)"/>
</svg>

<header class="site-header">
  <div class="brand"><span>TrindaMo</span><span class="brand-mark"></span></div>
  <div class="btn btn-signup">Sign Up</div>
  <div class="or">or</div>
  <div class="field-label" style="left:715px">Email :</div>
  <div class="field" style="left:713px"></div>
  <div class="field-label" style="left:906px">Password :</div>
  <div class="field" style="left:905px"></div>
  <div class="btn btn-login">Login</div>
  <div class="keep"><span class="box"></span>Keep me logged in</div>
  <div class="forgot">Forgot your password?</div>
</header>

<svg class="feature" viewBox="0 0 520 520" aria-hidden="true">
  <circle cx="260" cy="260" r="259" fill="rgba(255,255,255,.28)"/>
  <circle cx="260" cy="260" r="240" fill="var(--orange)" fill-opacity=".93"/>
</svg>

<main class="feature-copy">
  <svg class="basket" viewBox="0 0 68 68" aria-hidden="true">
    <path d="M24 26 L34 6 L44 26" fill="none" stroke="#4a4a4a" stroke-width="3"/>
    <rect x="6" y="26" width="56" height="9" rx="2" fill="#3aa8e0"/>
    <path d="M10 35 H58 L53 64 H15 Z" fill="#5bc3ee"/>
    <g stroke="#1f6f9c" stroke-width="3" stroke-linecap="round">
      <line x1="22" y1="41" x2="23" y2="57"/><line x1="30" y1="41" x2="30" y2="57"/>
      <line x1="38" y1="41" x2="38" y2="57"/><line x1="46" y1="41" x2="45" y2="57"/>
    </g>
  </svg>
  <h1 class="headline">SHOP DIRECTLY</h1>
  <p class="subline">FROM YOUR PROFILE</p>
  <div class="divider"></div>
  <p class="categories">
    <span class="hl">Active Life</span><span>Arts &amp; Entertainment</span><span class="hl">Automotive</span><span>Education</span><br>
    <span>Beauty &amp; Spas</span><span class="hl">Event Planning &amp; Services</span><span>Financial Services</span><br>
    <span class="hl">Health &amp; Medical</span><span>Home Services</span><span class="hl">Hotels</span><span>Pets</span><span class="hl">Nightlife</span><br>
    <span>Food</span><span class="hl">Local Services</span><span>Mass Media</span><span class="hl">Restaurant</span><span>Shopping</span><br>
    <span class="hl">Professional Services</span><span>Public Services &amp; Government</span>
  </p>
  <div class="divider divider-low"></div>
  <p class="search-label">SEARCH THE SITE</p>
  <span class="search-field"></span>
</main>

<nav class="footer-nav">
  <span>HOW IT WORKS</span><span class="dot"></span>
  <span>ABOUT US</span><span class="dot"></span>
  <span>BLOG</span><span class="dot"></span>
  <span>BUSINESS</span><span class="dot"></span>
  <span>JOBS</span><span class="dot"></span>
  <span>PRIVACY</span><span class="dot"></span>
  <span>FAQ</span><span class="dot"></span>
  <span>CONTACT</span>
</nav>
</body>
</html>
```